Non-Profit org for new mothers in distress in need of website design

We need a website for our non-profit organization, Cradlewell Alliance of Florida, based in Sarasota, Florida. We provide peer support for new moms in distress, trainings for mental health professionals, education and resources for our providers, and an intensive volunteer training program. We need a site that is calming yet energizing, simple, yet informative, with minimal pages and text. Our goal is to be a point of contact for mothers to find local resources whatever their need, so our most important feature we need is at least 4 zip code look-ups for users to find 1. Local volunteers, 2. Support Groups, 3. Trained Mental Health Professionals, 4. Other Health and Wellness Support Providers. Ideally I would like the zip code lookups on the home page sort of interest-layout-style, with the following pages: About Us, PPD Facts, For Parents, For Providers, Donate, Contact, and Blog. Because we are a very small non-profit - under 20 volunteers, no paid staff, donation funded, under $10,000 budget all going to service programs, we can't afford much, but are willing to pay a reasonable fee for quality work. Currently we have an active site through plonto... www.cradlewellhaven.org. The site either needs to be polished or overhauled. And we need a more professional zip code L/U. Thank you so much for your time and interest - we look forward to working with you.
Best,
Maren Tolliver

Reason: Hoping for a couple more changes and clearance with decision-making committee.

Target Market(s)

New mothers with babies and young children, new fathers and perinatal providers

Industry/Entity Type

Non Profit

Number of Pages Required

5+ page

Font styles to use
Sans Serif

Colors
886aae

Requirements
Must have
• contact form, zip code lookup, video embedded, calm and energizing tone
Nice to have
• boardly-style layout
Should not have
• complicated navigation, heavy text,

```html
<!DOCTYPE html>
<html lang="en">
<head>
<meta charset="utf-8">
<title>Cradlewell Alliance of Florida</title>
<link rel="stylesheet" href="https://fonts.googleapis.com/css2?family=Lato:ital,wght@0,300;0,400;0,700;1,300;1,400&display=swap">
<style>
  :root {
    --brand: #886aae;
    --brand-deep: #5c4878;
    --ink: #2f2f2f;
    --nav-muted: #a8a8a8;
    --body-muted: #b3b3b3;
    --white: #ffffff;
    --field-text: #b5b5b5;
  }
  * { box-sizing: border-box; margin: 0; padding: 0; }
  html, body { width: 1200px; height: 1000px; overflow: hidden; background: var(--white); }
  body { position: relative; font-family: "Lato", sans-serif; }

  .site-header {
    position: absolute; left: 0; top: 0; width: 1200px; height: 93px;
    background: var(--brand); border-bottom: 5px solid var(--brand-deep);
  }
  .brand { position: absolute; left: 463px; top: 22px; display: flex; align-items: center; gap: 10px; color: var(--white); }
  .brand-dot { width: 42px; height: 42px; border: 2px solid var(--white); border-radius: 50%; }
  .brand-name { font-size: 16px; font-weight: 400; line-height: 17px; }
  .brand-tagline { font-size: 12.5px; font-weight: 400; line-height: 15px; }

  .main-nav { position: absolute; top: 116px; left: 255px; display: flex; font-size: 17px; font-weight: 300; font-style: italic; color: var(--nav-muted); }
  .main-nav a { color: inherit; text-decoration: none; margin-right: 23px; }
  .main-nav a.is-current { color: #4a4a4a; }

  .photo { position: absolute; }
  .photo-mother { left: 91px; top: 253px; width: 195px; height: 300px; background: linear-gradient(180deg, #b9d4ef 0%, #f1e4de 50%, #a6b46b 100%); }
  .photo-newborn { left: 317px; top: 253px; width: 195px; height: 300px; background: linear-gradient(160deg, #4a3a30 0%, #b08f7c 55%, #6c5f55 100%); }
  .photo-laughing { left: 91px; top: 583px; width: 195px; height: 300px; background: linear-gradient(170deg, #f6efe9 0%, #e9c3a7 55%, #f3e2d4 100%); }
  .photo-feet { left: 316px; top: 583px; width: 195px; height: 150px; background: radial-gradient(circle at 55% 55%, #f0b9a1 0%, #fbe8df 70%, #fdf6f2 100%); }
  .photo-hands { left: 316px; top: 763px; width: 195px; height: 150px; background: linear-gradient(160deg, #3e3e22 0%, #8d7b63 50%, #9fb9d0 100%); }

  .hero-heading {
    position: absolute; left: 564px; top: 242px; width: 536px; text-align: center;
    font-size: 32px; font-weight: 300; font-style: italic; line-height: 38px; color: var(--ink);
  }
  .hero-copy {
    position: absolute; left: 573px; top: 380px; width: 524px;
    font-size: 17px; font-weight: 300; line-height: 21.6px; color: var(--body-muted);
  }
  .divider { position: absolute; left: 732px; top: 541px; width: 200px; height: 1px; background: #555; }

  .locator { position: absolute; left: 564px; top: 583px; width: 536px; height: 328px; background: var(--brand); }
  .field {
    position: absolute; background: var(--white); border-radius: 4px;
    font-size: 18px; font-weight: 700; color: var(--field-text);
    display: flex; align-items: center; justify-content: center;
  }
  .field-zip { left: 67px; top: 25px; width: 400px; height: 49px; }
  .field-select { left: 164px; top: 116px; width: 207px; height: 39px; }
  .field-select svg { position: absolute; right: 15px; top: 16px; }
  .find-button { left: 195px; top: 245px; width: 145px; height: 39px; color: var(--brand); }
</style>
</head>
<body>
  <header class="site-header">
    <div class="brand">
      <span class="brand-dot"></span>
      <div>
        <div class="brand-name">Cradlewell Alliance of Florida</div>
        <div class="brand-tagline">Mom Cares for Baby. We care for Mom.</div>
      </div>
    </div>
  </header>

  <nav class="main-nav">
    <a class="is-current" href="#">Home</a>
    <a href="#">About Us</a>
    <a href="#">PPD Facts</a>
    <a href="#">For Parents</a>
    <a href="#">For Providers</a>
    <a href="#">Donate</a>
    <a href="#">Contact</a>
    <a href="#">Blog</a>
  </nav>

  <div class="photo photo-mother" role="img" aria-label="Pregnant mother holding her young daughter's hand in a sunny field"></div>
  <div class="photo photo-newborn" role="img" aria-label="Newborn baby wrapped in a knit blanket"></div>
  <div class="photo photo-laughing" role="img" aria-label="Laughing baby held close by its mother"></div>
  <div class="photo photo-feet" role="img" aria-label="Parent's hands forming a heart around baby feet"></div>
  <div class="photo photo-hands" role="img" aria-label="Baby hand grasping an adult's fingers"></div>

  <h1 class="hero-heading">You are not alone.<br>You are not to blame.<br>With help and effort, you will be well.</h1>
  <p class="hero-copy">Find your Cradlewell Florida KindredMom Volunteer today with the locator below.&nbsp; Your area KindredMom will listen, connect you with Support Groups, counselors, therapists &amp; psychiatrists with training in PPD near you, doulas, wellness and more to encourage your PPD recovery.&nbsp; Your KindredMom is a trained volunteer and PPD overcomer - call or email her today.</p>
  <div class="divider"></div>

  <section class="locator">
    <div class="field field-zip">Enter zip code</div>
    <div class="field field-select">Select
      <svg width="13" height="7" viewBox="0 0 13 7"><path d="M0 0h13L6.5 7z" fill="#886aae"/></svg>
    </div>
    <div class="field find-button">Find</div>
  </section>
</body>
</html>
```